Logo for Internal Medicine practice

I want a logo for my Internal Medicine practice, I would like it to be with my name on it which is Lorena Benítez Prado.

I would like the business card to say the following (it is in Spanish since my practice is in Spanish):

Lorena Benítez Prado
Medicina Interna
Cel. 5587316420
lorenabenitezprado@correovela.com

Logo Text

Lorena Benítez

```html
<!DOCTYPE html>
<html lang="es">
<head>
<meta charset="utf-8">
<title>Lorena Benítez · Tarjeta de presentación</title>
<link rel="stylesheet" href="https://fonts.googleapis.com/css2?family=Nunito:wght@700;800&family=Arimo:wght@400&display=swap">
<style>
  :root {
    --backdrop: #2a2a2c;
    --card-white: #ffffff;
    --card-black: #141416;
    --brand-blue: #1c74c4;
    --brand-blue-light: #2a8ad8;
    --ink: #1b1b1b;
    --pattern-dark: #0b0b0c;
    --pattern-mid: #2c2c2f;
    --pattern-light: #8a8a8e;
  }
  * { box-sizing: border-box; margin: 0; padding: 0; }
  html, body {
    width: 1200px;
    height: 1108px;
    overflow: hidden;
    background: var(--backdrop);
  }
  .stage {
    width: 1200px;
    height: 1108px;
    display: flex;
    justify-content: center;
    align-items: center;
    gap: 90px;
  }
  .card {
    width: 350px;
    height: 580px;
    border-radius: 22px;
    position: relative;
    overflow: hidden;
    box-shadow: 0 18px 40px rgba(0, 0, 0, 0.45);
  }

  /* Front */
  .card--front {
    background: var(--card-white);
    display: flex;
    flex-direction: column;
    align-items: center;
    text-align: center;
  }
  .brand-mark {
    margin-top: 92px;
    width: 120px;
    height: 120px;
    background: var(--brand-blue);
  }
  .brand-name {
    margin-top: 22px;
    font-family: "Nunito", sans-serif;
    font-weight: 800;
    font-size: 38px;
    line-height: 1;
    color: var(--brand-blue);
  }
  .contact {
    margin-top: auto;
    margin-bottom: 62px;
    display: flex;
    flex-direction: column;
    align-items: center;
  }
  .contact__name {
    font-family: "Nunito", sans-serif;
    font-weight: 800;
    font-size: 24px;
    color: var(--brand-blue);
  }
  .contact__role {
    font-family: "Arimo", sans-serif;
    font-size: 18px;
    color: var(--ink);
    margin-top: 2px;
  }
  .contact__rule {
    width: 112px;
    height: 1.5px;
    background: var(--brand-blue);
    margin: 12px 0 10px;
  }
  .contact__phone {
    font-family: "Arimo", sans-serif;
    font-size: 19px;
    color: var(--ink);
    letter-spacing: 0.5px;
  }
  .contact__email {
    font-family: "Arimo", sans-serif;
    font-size: 15px;
    color: var(--ink);
    margin-top: 4px;
  }

  /* Back */
  .card--back {
    background: var(--card-black);
  }
  .back-pattern {
    position: absolute;
    inset: 0;
    background:
      radial-gradient(ellipse at 95% 8%, rgba(170, 170, 175, 0.55) 0%, rgba(170, 170, 175, 0) 55%),
      linear-gradient(215deg, var(--pattern-light) 0%, #4a4a4e 22%, var(--pattern-mid) 48%, var(--pattern-dark) 78%);
  }
  .back-brand {
    position: absolute;
    left: 0;
    right: 0;
    top: 408px;
    display: flex;
    justify-content: center;
    align-items: center;
    gap: 10px;
  }
  .back-brand__mark {
    width: 30px;
    height: 30px;
    background: var(--brand-blue-light);
  }
  .back-brand__name {
    font-family: "Nunito", sans-serif;
    font-weight: 800;
    font-size: 20px;
    color: var(--brand-blue-light);
  }
</style>
</head>
<body>
  <main class="stage">
    <section class="card card--front">
      <span class="brand-mark"></span>
      <h1 class="brand-name">Lorena Benítez</h1>
      <div class="contact">
        <p class="contact__name">Lorena Benítez Prado</p>
        <p class="contact__role">Medicina Interna</p>
        <span class="contact__rule"></span>
        <p class="contact__phone">5587316420</p>
        <p class="contact__email">lorenabenitezprado@correovela.com</p>
      </div>
    </section>

    <section class="card card--back">
      <div class="back-pattern" role="img" aria-label="Patrón repetido del monograma en barniz brillante sobre fondo negro, más claro en la esquina superior derecha"></div>
      <div class="back-brand">
        <span class="back-brand__mark"></span>
        <p class="back-brand__name">Lorena Benítez</p>
      </div>
    </section>
  </main>
</body>
</html>
```